The name of my company is Tolmen Refacing LLC and I would like the sub text to say "Cabinet Refacing and Countertops". Have my name Dorian Tolmen, Owner / Sales, contact info: Cell: 360-555-0147 / Email: dorian.tolmen@quenmail.com

Simple, Clean, and Organized. With colors that will appeal to the eye.

Target Market(s)

Houses and Apartments

Industry/Entity Type

Cabinet Refacing

Contact Information for Business Card

Company name and sub text Dorian Tolmen - Owner / Sales, my cell phone number and email

Requirements
Must have
• Business name, my name / position, and my contact info
Nice to have
• Simple. Organized. Appealing to the eye

```html
<!DOCTYPE html>
<html lang="en">
<head>
<meta charset="utf-8">
<title>Tolmen Refacing LLC — Business Card</title>
<link href="https://fonts.googleapis.com/css2?family=Montserrat:wght@300;400;500;700&display=swap" rel="stylesheet">
<style>
  :root {
    --stage: #3a3a3d;
    --card: #262627;
    --accent: #4a6fb8;
    --text-light: #d9dce3;
    --text-muted: #b9bcc4;
  }
  * { box-sizing: border-box; margin: 0; padding: 0; }
  html, body { width: 1200px; height: 900px; overflow: hidden; }
  body {
    background: var(--stage);
    font-family: "Montserrat", sans-serif;
    position: relative;
  }
  .card {
    position: absolute;
    width: 560px;
    height: 320px;
    background: var(--card);
    border-radius: 22px;
    overflow: hidden;
    box-shadow: 0 18px 40px rgba(0,0,0,0.45);
  }
  .card--back { left: 80px; top: 90px; }
  .card--front { left: 560px; top: 490px; }

  .accent-band {
    position: absolute;
    background: var(--accent);
  }
  .card--back .accent-band { left: 0; right: 0; bottom: 0; height: 70px; }
  .card--front .accent-band { top: 0; bottom: 0; right: 0; width: 120px; }

  .brand { position: absolute; color: var(--text-light); }
  .brand__name {
    font-weight: 400;
    letter-spacing: 0.06em;
    text-transform: uppercase;
    line-height: 1.1;
  }
  .brand__tagline {
    font-weight: 400;
    letter-spacing: 0.08em;
    text-transform: uppercase;
    color: var(--text-muted);
  }
  .card--back .brand {
    top: 72px; left: 0; right: 0; text-align: center;
  }
  .card--back .brand__name { font-size: 30px; }
  .card--back .brand__tagline { font-size: 12.5px; margin-top: 8px; }

  .card--front .brand { top: 44px; left: 40px; }
  .brand__row { display: flex; align-items: center; gap: 12px; }
  .brand__mark { width: 22px; height: 22px; background: var(--accent); flex: none; }
  .card--front .brand__name { font-size: 27px; }
  .card--front .brand__tagline { font-size: 12px; margin-top: 8px; margin-left: 34px; }

  .person { position: absolute; left: 40px; top: 168px; }
  .person__name { color: var(--accent); font-weight: 700; font-size: 24px; }
  .person__role { color: var(--text-light); font-weight: 400; font-size: 14px; margin-top: 2px; }

  .contact { position: absolute; left: 40px; top: 240px; list-style: none; }
  .contact__item {
    display: flex; align-items: center; gap: 10px;
    color: var(--text-light); font-size: 14px; line-height: 1.7;
  }
  .contact__icon { width: 13px; height: 13px; fill: var(--accent); flex: none; }
</style>
</head>
<body>

  <section class="card card--back" aria-label="Business card back">
    <div class="brand">
      <div class="brand__name">Tolmen Refacing, LLC</div>
      <div class="brand__tagline">Cabinet Refacing and Countertops</div>
    </div>
    <div class="accent-band"></div>
  </section>

  <section class="card card--front" aria-label="Business card front">
    <div class="accent-band"></div>
    <div class="brand">
      <div class="brand__row">
        <span class="brand__mark"></span>
        <span class="brand__name">Tolmen Refacing, LLC</span>
      </div>
      <div class="brand__tagline">Cabinet Refacing and Countertops</div>
    </div>

    <div class="person">
      <div class="person__name">Dorian Tolmen</div>
      <div class="person__role">Owner / Sales</div>
    </div>

    <ul class="contact">
      <li class="contact__item">
        <svg class="contact__icon" viewBox="0 0 24 24" aria-hidden="true"><path d="M6.6 10.8a15.1 15.1 0 0 0 6.6 6.6l2.2-2.2a1 1 0 0 1 1-.25 11.4 11.4 0 0 0 3.6.57 1 1 0 0 1 1 1V20a1 1 0 0 1-1 1A17 17 0 0 1 3 4a1 1 0 0 1 1-1h3.5a1 1 0 0 1 1 1c0 1.25.2 2.45.57 3.57a1 1 0 0 1-.25 1z"/></svg>
        360-555-0147
      </li>
      <li class="contact__item">
        <svg class="contact__icon" viewBox="0 0 24 24" aria-hidden="true"><path d="M2 5h20v14H2z M4 7v.5l8 5 8-5V7l-8 5z" fill-rule="evenodd"/></svg>
        dorian.tolmen@quenmail.com
      </li>
    </ul>
  </section>

</body>
</html>
```